DRIFTFRAME studio

Design to be modern with colours of logo, maybe orange background. Include name, position, phone/WhatsApp email/web. Specialises in long form TIMELAPSE

Contact Information for Business Card

Marcel Okoro, filmmaker,/photographer, phone/WhatsApp +971529386047, email - marcel@driftframestudio.com www.driftframestudio.com, instagram @driftframestudio

Font styles to use
Sans Serif

Requirements
Must have
• Fresh, bright, modern, original
Marcel Okoro - Filmmaker/Photographer
Phone/WhatsApp +971 529 38 6047
email - marcel@driftfarmestudio.com
Web - driftfarmestudio.com
PoBox 584319, Dubai, UAE
instagram - driftframestudio
Should not have
• solid black background

```html
<!DOCTYPE html>
<html lang="en">
<head>
<meta charset="utf-8">
<title>DRIFTFRAME studio — Business Card</title>
<link href="https://fonts.googleapis.com/css2?family=Montserrat:wght@600;700&family=Prompt:wght@400&display=swap" rel="stylesheet">
<style>
  :root {
    --orange: #f47524;
    --white: #ffffff;
    --ink: #111111;
    --backdrop: #e9e9e9;
  }
  * { margin: 0; padding: 0; box-sizing: border-box; }
  html, body { width: 1200px; height: 900px; overflow: hidden; }
  body {
    background: var(--backdrop);
    font-family: "Prompt", sans-serif;
    position: relative;
  }
  .card {
    position: absolute;
    left: 250px;
    width: 700px;
    height: 400px;
    background: var(--orange);
    overflow: hidden;
    box-shadow: 0 6px 18px rgba(0,0,0,0.18);
  }
  .card-front { top: 35px; }
  .card-back { top: 465px; }

  .brand-name {
    font-family: "Montserrat", sans-serif;
    font-weight: 700;
    text-transform: uppercase;
    letter-spacing: 1px;
    line-height: 1;
    display: flex;
    align-items: center;
    white-space: nowrap;
  }
  .brand-words span { display: block; }
  .brand-words span + span { padding-left: 0.6em; }
  .brand-mark {
    display: inline-block;
    border-radius: 50%;
    border: 5px solid currentColor;
    flex: none;
  }
  .front-brand {
    position: absolute;
    left: 0; right: 0; top: 128px;
    justify-content: center;
    color: var(--white);
    font-size: 50px;
    gap: 22px;
  }
  .front-brand .brand-mark { width: 104px; height: 104px; }
  .front-web {
    position: absolute;
    left: 0; right: 0; bottom: 34px;
    text-align: center;
    color: var(--white);
    font-size: 20px;
    letter-spacing: 0.5px;
  }

  .back-brand {
    position: absolute;
    left: 30px; top: 140px;
    color: var(--ink);
    font-size: 30px;
    gap: 12px;
  }
  .back-brand .brand-mark { width: 70px; height: 70px; border-width: 4px; }
  .divider {
    position: absolute;
    left: 380px;
    width: 2px;
    background: var(--white);
  }
  .divider-name { top: 112px; height: 52px; }
  .divider-contact { top: 190px; height: 110px; }

  .person { position: absolute; left: 400px; top: 110px; color: var(--white); }
  .person-name {
    font-family: "Montserrat", sans-serif;
    font-weight: 700;
    font-size: 24px;
    letter-spacing: 6px;
    text-transform: uppercase;
    line-height: 30px;
  }
  .person-role { color: var(--ink); font-size: 17px; margin-top: 2px; }

  .contact-list {
    position: absolute;
    left: 398px; top: 188px;
    list-style: none;
    color: var(--ink);
    font-size: 18px;
    line-height: 28px;
  }
  .contact-list li { display: flex; align-items: center; gap: 12px; }
  .contact-list svg { width: 18px; height: 18px; flex: none; }

  .address-band {
    position: absolute;
    left: 0; right: 0; top: 318px; height: 42px;
    background: var(--white);
    color: var(--orange);
    font-size: 20px;
    line-height: 42px;
    padding-left: 270px;
  }
</style>
</head>
<body>

  <section class="card card-front" aria-label="Card front">
    <div class="brand-name front-brand"><span class="brand-mark"></span><span class="brand-words"><span>Driftframe</span><span>studio</span></span></div>
    <p class="front-web">www.driftframestudio.com</p>
  </section>

  <section class="card card-back" aria-label="Card back">
    <div class="brand-name back-brand"><span class="brand-mark"></span><span class="brand-words"><span>Driftframe</span><span>studio</span></span></div>

    <span class="divider divider-name"></span>
    <div class="person">
      <h1 class="person-name">Marcel Okoro</h1>
      <p class="person-role">Flmmaker/photographer</p>
    </div>

    <span class="divider divider-contact"></span>
    <ul class="contact-list">
      <li>
        <svg viewBox="0 0 24 24" fill="none" stroke="#fff" stroke-width="2"><path d="M5 3h4l2 5-2.5 1.5a11 11 0 0 0 6 6L16 13l5 2v4a2 2 0 0 1-2 2A16 16 0 0 1 3 5a2 2 0 0 1 2-2z"/></svg>
        +971 529 38 6047
      </li>
      <li>
        <svg viewBox="0 0 24 24" fill="none" stroke="#fff" stroke-width="2"><circle cx="12" cy="12" r="9"/></svg>
        @driftframestudio
      </li>
      <li>
        <svg viewBox="0 0 24 24" fill="none" stroke="#fff" stroke-width="2"><rect x="3" y="5" width="18" height="14"/><path d="M3 5l9 8 9-8"/></svg>
        marcel@driftframestudio.com
      </li>
      <li>
        <svg viewBox="0 0 24 24" fill="none" stroke="#fff" stroke-width="2"><circle cx="12" cy="12" r="9"/><path d="M3 12h18M12 3c3 3 3 15 0 18M12 3c-3 3-3 15 0 18"/></svg>
        www.driftframestudio.com
      </li>
    </ul>

    <p class="address-band">PoBox 584319, Dubai, UAE</p>
  </section>

</body>
</html>
```